Advertising flyer for proofreading business.

Hello everyone,

I need an advertising flyer for a new proofreading company in Australia.

I would like your design in be in two sizes:
- A4 (to be posted on noticeboards),
- A6 (to be printed in larger quantity to give away)
(please see the size specification file attached).

The text file is attached (Ad Text) and it contains lots of information. Please feel free to include your choice of text from the text file, but please include Poster title, and highlight 'ESL' and students discounts.

I understand that it is impossible to include the same amount of information on A6 and A4, so please feel free to chose what fits on each of them, but please keep the design similar.

I have attached our company logo, but feel free to adjust it to the poster design (feel free to change the color as well). The original logo file contains circle around it, please feel free to remove it and include only the typeset as it can be seen here: http://www.lexmarka.com.au/.

Flyers will be printed, so please see the specification file for details.

I will do my best to respond to feedback as soon as possible.

I appreciate your participation, time and help,
Best wishes,
Bartosz

Target Market(s)

Students, authors

Industry/Entity Type

Business

Colors

Designer to choose colors to be used in the design.

Requirements
Must have
• It would be good if poster is easy to spot on busy noticeboards and attract attention.
• Please keep the poster in the positive/optimistic mood, and so that it focuses on students, maybe photos of graduates(?).
• Poster title,
• Please include the list of proof-read documents as they are described in the attached text file (Ad Text).
• Please highlight students discounts and ESL.
Nice to have
• I would like to leave the creative freedom to all designers so at this point I have not adjusted the Look and Feel sliders. Please feel free to offer your own take on this.
• It would be nice if most of the text could be fit to the poster.

```html
<!DOCTYPE html>
<html lang="en">
<head>
<meta charset="utf-8">
<title>Clearpage – proofreading flyer</title>
<link href="https://fonts.googleapis.com/css2?family=Bebas+Neue&family=Open+Sans:wght@400;600;700&display=swap" rel="stylesheet">
<style>
:root{
  --bg:#6b6b6b;
  --teal:#1bbf9c;
  --green:#4aab8a;
  --green-text:#3fa57e;
  --slate:#515255;
  --ink:#3c3c3c;
  --white:#ffffff;
}
*{box-sizing:border-box;margin:0;padding:0}
html,body{width:913px;height:1200px;overflow:hidden;background:var(--bg)}
body{font-family:"Open Sans",Arial,sans-serif;color:var(--ink)}
.flyer{position:absolute;left:84px;top:75px;width:740px;height:1047px;background:var(--white);overflow:hidden}
.hero{position:absolute;left:0;top:0;width:740px;height:353px;
  background:linear-gradient(100deg,#b9b7b6 0%,#8e8683 35%,#6f6a69 60%,#a5a3a4 100%)}
.brand{position:absolute;left:112px;top:65px;width:192px;height:192px;border-radius:50%;background:var(--teal);
  display:flex;align-items:center;justify-content:center;color:var(--white);font-size:32px;font-weight:400}
.hero-title{position:absolute;left:0;right:0;top:292px;text-align:center;color:var(--white);font-size:27px;font-weight:600}
.esl{position:absolute;left:0;top:353px;width:740px;height:194px}
.esl-title{position:absolute;left:0;right:0;top:38px;text-align:center;font-family:"Bebas Neue",Impact,sans-serif;font-size:38px;color:var(--ink);letter-spacing:.3px}
.esl-title span{color:var(--green-text)}
.feature{position:absolute;display:flex;align-items:center;gap:14px;font-size:12.5px;line-height:15px;color:var(--ink)}
.feature svg{flex:none}
.feature.native{left:79px;top:110px}
.feature.native p{width:192px}
.feature.scope{left:374px;top:104px}
.feature.scope p{width:240px}
.docs{position:absolute;left:0;top:547px;width:370px;height:332px;background:var(--slate);color:#eee}
.prices{position:absolute;left:370px;top:547px;width:370px;height:332px;background:var(--green);color:var(--white)}
.panel-head{height:53px;border-bottom:1px solid rgba(255,255,255,.55);display:flex;align-items:center;justify-content:center;font-size:19px;font-weight:700;color:var(--white)}
.doc-row{position:absolute;left:0;width:370px;display:flex;justify-content:center;align-items:center;font-size:15px;line-height:18px;text-align:center}
.doc-row span{padding:0 16px;border-left:2px solid var(--teal)}
.doc-row span:first-child{border-left:none}
.price{position:absolute;text-align:center;font-size:15px;line-height:18px}
.quote{position:absolute;left:0;top:879px;width:740px;height:101px;text-align:center;font-size:14.5px;line-height:18px;color:var(--ink);padding:21px 60px 0}
.quote cite{display:block;font-style:normal;font-weight:600;margin-top:8px}
.contact{position:absolute;left:0;top:980px;width:740px;height:67px;background:var(--green);color:var(--white);display:flex;align-items:center;justify-content:center;font-size:16.5px}
.contact b{font-weight:700;margin-left:5px}
</style>
</head>
<body>
<main class="flyer">
  <section class="hero" role="img" aria-label="Photo of a smiling student holding books in a library, with classmates reading in the background">
    <div class="brand">Clearpage</div>
    <p class="hero-title">Professional, English language proofreading</p>
  </section>

  <section class="esl">
    <h1 class="esl-title">Help with <span>English as a second language</span> (ESL)</h1>
    <div class="feature native">
      <svg width="43" height="43" viewBox="0 0 43 43"><circle cx="21.5" cy="21.5" r="21.5" fill="#2fb394"/><circle cx="21.5" cy="16" r="6" fill="#fff"/><path d="M11 32c1-7 5-9 10.5-9S31 25 32 32z" fill="#fff"/></svg>
      <p>Proofreading by a native English speaker with an English Honours degree.</p>
    </div>
    <div class="feature scope">
      <svg width="43" height="43" viewBox="0 0 43 43"><circle cx="21.5" cy="21.5" r="21.5" fill="#2fb394"/><g stroke="#fff" stroke-width="2.4" stroke-linecap="round"><path d="M11 14l2 2 3-4M11 21l2 2 3-4"/><path d="M19 14h13M19 21h13M19 28h13M12 28h2"/></g></svg>
      <p>Includes correct all English language errors, spelling and grammar mistakes, reference checking and editing for style, coherence and clarity.</p>
    </div>
  </section>

  <section class="docs">
    <h2 class="panel-head">We will proofread your</h2>
    <div class="doc-row" style="top:69px"><span>essays &amp;<br>assignments</span><span>training<br>manuals</span><span>presentations<br>&amp; speeches</span></div>
    <div class="doc-row" style="top:136px"><span style="padding:8px 28px">theses</span><span style="padding:8px 28px">newsletters</span><span style="padding:8px 28px">websites</span></div>
    <div class="doc-row" style="top:196px"><span>resumes</span><span>advertising<br>copy</span><span>novels &amp; short<br>stories</span></div>
    <div class="doc-row" style="top:267px"><span>business<br>correspondence</span><span>brochures, catalogues<br>&amp; media releases</span></div>
  </section>

  <section class="prices">
    <h2 class="panel-head">Price guide</h2>
    <p class="price" style="left:20px;width:152px;top:84px">Prices start at only $20 (short menus, flyers, letters).</p>
    <p class="price" style="left:184px;width:162px;top:80px">Discounts for not-for-profit organisations and students.</p>
    <p class="price" style="left:8px;width:168px;top:162px">Great student discount rate: $25 per hour (roughly 1000 words - 4 pages - of well-written text).</p>
    <p class="price" style="left:189px;width:150px;top:176px">Package deals on documents over 50,000 words.</p>
    <p class="price" style="left:0;width:370px;top:270px">Fast, negotiable time-frames (same day<br>service available by special arrangement).</p>
  </section>

  <blockquote class="quote">
    “Clara understood our requirements quickly and has been fantastic at delivering quality work, on time and within agreed budget. It’s a pleasure to work with her.”
    <cite>Ruth Palmer, Operations Manager, northwaveAU</cite>
  </blockquote>

  <footer class="contact">Contact us for an obligation free quote:<b>0400 555 123 / proofing@clearpage.com.au.</b></footer>
</main>
</body>
</html>
```